QUILLDESK - Remote Tech Support Site

We are looking for a new very responsive and simple website for our brand Quilldesk.com - a remote technical support company.

This company supports customers Globally in different countries throughout Eur/ North America / South America / Asia etc (please keep this in mind and integrate into the idea).

Its important to us that the design is very explanatory, the customer should easily be able to figure out that we provide computer support right away ... I like one page responsive type designs as well without a bunch of menu items

Here are some similar sites we like - but still looking for a unique design that fits out brand "quilldesk" - I have upload also some layouts i like (but the designs are not important just the layouts), youll see it includes consumer business etc which is important.

MORVEL.COM - I love how clean it is - nice and white easy to see everything

PIXOLANE247.COM - also nice the layout and responsive one page design makes it easy to use

brightfixhub.com - similar to pixolane design as well - you can get the idea im looking for between the two

You will notice those examples are much different then the attachments I added - again this is more of an idea for possible layouts .. attached is also the logo - could inspire color scheme / blue white black etc

Target Market(s)

Home consumers without computer knowledge , older age 45-65, small medium business ... computer repair - slow computers

Industry/Entity Type

Computer Repair

Logo Text

Quilldesk

Coding

Coded - Design and coding required

Number of Pages Required

1 page

Font styles to use
Sans Serif
Other font styles liked:
• your choice responsive

Colors

Designer to choose colors to be used in the design.

Requirements
Must have
• Clean - responsive - professional design - the name says it all - quilldesk
• CALL TO ACTIONS FOR "Get Help Now!" / "Learn More" etc
Nice to have
• We are looking for a new very responsive and simple website for our brand Quilldesk.com - a remote technical support company.
• This company supports customers Globally in different countries throughout Eur/ North America / South America / Asia etc (please keep this in mind and integrate into the idea).
• Its important to us that the design is very explanatory, the customer should easily be able to figure out that we provide computer support right away ... I like one page responsive type designs as well without a bunch of menu items
• Here are some similar sites we like - but still looking for a unique design that fits out brand "quilldesk" - I have upload also some layouts i like (but the designs are not important just the layouts), youll see it includes consumer business etc which is important.
• MORVEL.COM - I love how clean it is - nice and white easy to see everything
• PIXOLANE247.COM - also nice the layout and responsive one page design makes it easy to use
• brightfixhub.com - similar to pixolane design as well - you can get the idea im looking for between the two
Should not have
• dark, packed page - bad small font -

```html
<!DOCTYPE html>
<html lang="en">
<head>
<meta charset="utf-8">
<title>Quilldesk – Dedicated Support Anytime Anywhere</title>
<link rel="stylesheet" href="https://fonts.googleapis.com/css2?family=Michroma&family=Open+Sans:wght@400;600;700&display=swap">
<style>
  :root {
    --blue: #1b8ff0;
    --blue-deep: #0f6fcf;
    --ink: #1f2a33;
    --text: #3a4650;
    --muted: #6b7782;
    --hero-top: #c9d1d7;
    --hero-mid: #eef1f3;
    --white: #ffffff;
    --star: #f5a623;
  }
  * { box-sizing: border-box; margin: 0; padding: 0; }
  html, body { width: 1200px; height: 947px; overflow: hidden; background: var(--white); }
  body { font-family: "Open Sans", sans-serif; color: var(--text); position: relative; }

  .hero {
    position: absolute; left: 0; top: 0; width: 1200px; height: 470px;
    background: linear-gradient(160deg, var(--hero-top) 0%, var(--hero-mid) 55%, #f7f8f9 100%);
  }
  .site-header {
    position: absolute; left: 0; top: 0; width: 100%; height: 84px;
    display: flex; align-items: center; padding: 0 70px;
  }
  .brand { display: flex; align-items: center; gap: 10px; font-size: 26px; font-weight: 600; color: var(--blue); }
  .brand-dot { width: 30px; height: 30px; border-radius: 50%; background: var(--blue); }
  .call { margin-left: auto; display: flex; align-items: center; gap: 10px; color: var(--muted); }
  .call-label { font-size: 11px; display: block; }
  .call-number { font-size: 17px; color: var(--text); }
  .btn {
    display: inline-block; background: var(--blue); color: var(--white);
    font-size: 12px; font-weight: 700; letter-spacing: .5px; text-transform: uppercase;
    padding: 12px 22px;
  }
  .btn-help { margin-left: 28px; }

  .hero-copy { position: absolute; left: 70px; top: 178px; }
  .hero-kicker { font-family: "Michroma", sans-serif; font-size: 17px; color: var(--ink); letter-spacing: .5px; }
  .hero-title { font-family: "Michroma", sans-serif; font-weight: 400; font-size: 30px; color: var(--ink); letter-spacing: 1px; margin-top: 2px; }
  .perks { list-style: none; display: grid; grid-template-columns: 190px 190px; gap: 12px 0; margin-top: 24px; font-size: 13px; }
  .perks li, .benefits li { display: flex; align-items: center; gap: 9px; }
  .perks b { color: var(--ink); }
  .btn-outline {
    display: inline-block; margin-top: 28px; border: 1px solid var(--white); color: var(--white);
    font-size: 12px; font-weight: 700; padding: 10px 22px; background: rgba(255,255,255,.15);
  }
  .hero-art {
    position: absolute; right: 40px; top: 110px; width: 520px; height: 340px;
    background: radial-gradient(ellipse at 55% 55%, #8ab3da 0%, #bccedf 45%, rgba(230,236,240,0) 75%);
  }
  .scroll-down {
    position: absolute; left: 582px; top: 452px; width: 36px; height: 36px; border-radius: 50%;
    background: var(--white); display: flex; align-items: center; justify-content: center; z-index: 2;
    box-shadow: 0 2px 6px rgba(0,0,0,.15);
  }

  .reviews {
    position: absolute; left: 0; top: 470px; width: 1200px; height: 180px; background: var(--blue);
    display: flex; gap: 110px; padding: 46px 70px 0 110px; color: var(--white);
  }
  .review { width: 400px; }
  .review-head { display: flex; align-items: center; gap: 12px; font-size: 19px; font-weight: 600; }
  .review-mark { width: 34px; height: 34px; border-radius: 50%; background: var(--blue-deep); }
  .review-mark.is-star { background: var(--star); }
  .review p { font-size: 12px; line-height: 1.6; margin: 12px 0 0 46px; opacity: .9; }

  .features { position: absolute; left: 0; top: 650px; width: 1200px; height: 297px; background: var(--white); }
  .features-art {
    position: absolute; left: 150px; top: 26px; width: 300px; height: 246px;
    background: linear-gradient(180deg, #f3f5f7 0%, #d9e2ea 100%);
  }
  .features-copy { position: absolute; left: 560px; top: 34px; }
  .features-kicker { font-family: "Michroma", sans-serif; font-size: 13px; color: var(--ink); }
  .features-title { font-family: "Michroma", sans-serif; font-weight: 400; font-size: 20px; color: var(--ink); margin-top: 2px; }
  .benefits { list-style: none; margin-top: 22px; font-size: 13px; color: var(--text); display: grid; gap: 14px; }
  .benefits li:nth-child(2), .benefits li:nth-child(3) { margin-left: 14px; }
  .btn-start { margin-top: 22px; }
</style>
</head>
<body>
  <section class="hero">
    <header class="site-header">
      <div class="brand"><span class="brand-dot"></span>quilldesk</div>
      <div class="call">
        <svg width="16" height="26" viewBox="0 0 16 26" aria-hidden="true"><rect x="1" y="1" width="14" height="24" rx="2" fill="none" stroke="#1b8ff0" stroke-width="2"/><circle cx="8" cy="21" r="1.5" fill="#1b8ff0"/></svg>
        <div><span class="call-label">Call now :</span><span class="call-number">(555) 014-2287</span></div>
      </div>
      <a class="btn btn-help">Get Help Now!</a>
    </header>

    <div class="hero-copy">
      <p class="hero-kicker">DEDICATED SUPPORT</p>
      <h1 class="hero-title">ANYTIME . ANYWHERE</h1>
      <ul class="perks">
        <li><svg width="13" height="13" viewBox="0 0 13 13" aria-hidden="true"><circle cx="6.5" cy="6.5" r="6.5" fill="#1b8ff0"/><path d="M3.5 6.7l2 2 4-4" fill="none" stroke="#fff" stroke-width="1.6"/></svg><span><b>Instant</b> Support</span></li>
        <li><svg width="13" height="13" viewBox="0 0 13 13" aria-hidden="true"><circle cx="6.5" cy="6.5" r="6.5" fill="#1b8ff0"/><path d="M3.5 6.7l2 2 4-4" fill="none" stroke="#fff" stroke-width="1.6"/></svg><span><b>Quick</b> Setup &amp; Install</span></li>
        <li><svg width="13" height="13" viewBox="0 0 13 13" aria-hidden="true"><circle cx="6.5" cy="6.5" r="6.5" fill="#1b8ff0"/><path d="M3.5 6.7l2 2 4-4" fill="none" stroke="#fff" stroke-width="1.6"/></svg><span><b>Real - Time</b> Optimization</span></li>
        <li><svg width="13" height="13" viewBox="0 0 13 13" aria-hidden="true"><circle cx="6.5" cy="6.5" r="6.5" fill="#1b8ff0"/><path d="M3.5 6.7l2 2 4-4" fill="none" stroke="#fff" stroke-width="1.6"/></svg><span><b>Leading</b> Security Software</span></li>
        <li><svg width="13" height="13" viewBox="0 0 13 13" aria-hidden="true"><circle cx="6.5" cy="6.5" r="6.5" fill="#1b8ff0"/><path d="M3.5 6.7l2 2 4-4" fill="none" stroke="#fff" stroke-width="1.6"/></svg><span><b>Free</b> Diagnostic</span></li>
        <li><svg width="13" height="13" viewBox="0 0 13 13" aria-hidden="true"><circle cx="6.5" cy="6.5" r="6.5" fill="#1b8ff0"/><path d="M3.5 6.7l2 2 4-4" fill="none" stroke="#fff" stroke-width="1.6"/></svg><span><b>Unlimited</b> Cloud Backup</span></li>
      </ul>
      <a class="btn-outline">LEARN MORE</a>
    </div>

    <div class="hero-art" role="img" aria-label="Illustration of a laptop surrounded by blue security shields"></div>
  </section>

  <div class="scroll-down">
    <svg width="12" height="8" viewBox="0 0 12 8" aria-hidden="true"><path d="M1 1l5 5 5-5" fill="none" stroke="#3a4650" stroke-width="1.8"/></svg>
  </div>

  <section class="reviews">
    <article class="review">
      <div class="review-head"><span class="review-mark"></span>Chatterly</div>
      <p>Friendly technicians fixed my slow laptop in minutes. Clear steps, patient help and no jargon at all. I would happily call again.</p>
    </article>
    <article class="review">
      <div class="review-head"><span class="review-mark is-star"></span>REVIEWNEST</div>
      <p>Rated excellent by thousands of home and business customers across Europe, the Americas and Asia for fast remote support.</p>
    </article>
  </section>

  <section class="features">
    <div class="features-art" role="img" aria-label="Photo of a happy customer with arms raised behind a laptop"></div>
    <div class="features-copy">
      <p class="features-kicker">REALTIME SUPPORT</p>
      <h2 class="features-title">FEATURES AND BENEFITS</h2>
      <ul class="benefits">
        <li><svg width="11" height="11" viewBox="0 0 11 11" aria-hidden="true"><circle cx="5.5" cy="5.5" r="4.3" fill="none" stroke="#1b8ff0" stroke-width="2"/></svg>24/7 Real-Time Technician Support</li>
        <li><svg width="11" height="11" viewBox="0 0 11 11" aria-hidden="true"><circle cx="5.5" cy="5.5" r="4.3" fill="none" stroke="#1b8ff0" stroke-width="2"/></svg>The best Security Software in the market</li>
        <li><svg width="11" height="11" viewBox="0 0 11 11" aria-hidden="true"><circle cx="5.5" cy="5.5" r="4.3" fill="none" stroke="#1b8ff0" stroke-width="2"/></svg>Regular tune-ups and optimization</li>
        <li><svg width="11" height="11" viewBox="0 0 11 11" aria-hidden="true"><circle cx="5.5" cy="5.5" r="4.3" fill="none" stroke="#1b8ff0" stroke-width="2"/></svg>Setup and installation included</li>
      </ul>
      <a class="btn btn-start">Get Started</a>
    </div>
  </section>
</body>
</html>
```